Vetrune
@PEmmo, #128 looks good. Could I see some designs for other stationeries? Thanks
@Lumetra - #130 looks good thanks. I think we need phone number on the letterhead.
Thank you all for the inputs - these are great designs.
@Quorby, for #127, I dont think we need phone and email on the envelope. We can leave the web address. thanks.
@Lumetra - i like the idea of #96. But i dont like the black back. I like an orange back as shown #87. Also, the contact info should probably be left aligned with the logo on top.
Thanks for the inputs. I am not a fan of the color black.
@Dorvel, Could you please make the logo bigger in #91?
Dear Ju,
Pls see private message from the top right of the page..
Thanks..
Thanks for the inputs Quorby. I like #64. Would we see a variety in the font color?
Please, please - do not post pre-made templates or templates that were used in a previous contest. It does nothing but kill your credibility.

```html
<!DOCTYPE html>
<html lang="en">
<head>
<meta charset="utf-8">
<title>Vetrune business card</title>
<link href="https://fonts.googleapis.com/css2?family=Varela+Round&family=Roboto:wght@400;700&display=swap" rel="stylesheet">
<style>
  :root {
    --bg: #e9e7e4;
    --card: #ffffff;
    --ink: #111111;
    --ink-soft: #333333;
    --rule: #555555;
    --mark-blue: #2a7fd4;
  }
  html, body {
    margin: 0;
    width: 1200px;
    height: 1028px;
    overflow: hidden;
    background: var(--bg);
  }
  .canvas {
    position: relative;
    width: 1200px;
    height: 1028px;
  }
  .card-shape {
    position: absolute;
    left: 0;
    top: 0;
    filter: drop-shadow(0 6px 10px rgba(0,0,0,0.25));
  }
  .card-text {
    position: absolute;
    font-family: "Roboto", Arial, sans-serif;
    color: var(--ink-soft);
    margin: 0;
    white-space: nowrap;
  }
  .brand-name {
    font-family: "Varela Round", "Century Gothic", sans-serif;
    color: var(--ink);
    font-size: 56px;
    line-height: 1;
    letter-spacing: -1px;
  }
  .tagline {
    font-size: 10px;
    font-weight: 700;
    color: var(--ink);
    letter-spacing: 0.1px;
  }
  .person-name { font-size: 13px; font-weight: 700; color: var(--ink); }
  .person-title { font-size: 10.5px; }
  .address, .contact { font-size: 10.5px; line-height: 15px; }
  .contact {
    border-left: 1.5px solid var(--rule);
    padding-left: 10px;
  }
  .contact span { display: inline-block; width: 38px; }
  .web { font-size: 14px; color: var(--ink); }
</style>
</head>
<body>
<div class="canvas">
  <svg class="card-shape" width="1200" height="1028" viewBox="0 0 1200 1028">
    <defs>
      <radialGradient id="faint-mark" cx="50%" cy="50%" r="50%">
        <stop offset="0%" stop-color="#e2ebf5"/>
        <stop offset="60%" stop-color="#f2f1ea"/>
        <stop offset="100%" stop-color="#ffffff" stop-opacity="0"/>
      </radialGradient>
    </defs>
    <g class="card-back" fill="var(--card)">
      <rect x="440" y="528" width="520" height="306" rx="14"/>
      <circle cx="865" cy="590" r="98"/>
      <circle cx="918" cy="650" r="110"/>
      <circle cx="925" cy="760" r="86"/>
    </g>
    <circle cx="870" cy="680" r="150" fill="url(#faint-mark)" role="img" aria-label="Faint large brand emblem decoration"/>
    <g class="card-front" fill="var(--card)">
      <rect x="264" y="172" width="459" height="334" rx="14"/>
      <circle cx="282" cy="290" r="100"/>
      <circle cx="272" cy="410" r="96"/>
    </g>
    <circle cx="300" cy="390" r="125" fill="url(#faint-mark)" role="img" aria-label="Faint large brand emblem decoration"/>
    <circle class="brand-dot" cx="400" cy="268" r="44" fill="var(--mark-blue)"/>
    <circle class="brand-dot" cx="537" cy="729" r="46" fill="var(--mark-blue)"/>
  </svg>

  <p class="card-text brand-name" style="left:462px; top:243px;">Vetrune</p>
  <p class="card-text tagline" style="left:466px; top:310px;">IT SOLUTIONS TAILORED FOR YOUR BUSINESS</p>

  <p class="card-text person-name" style="left:467px; top:356px;">Dana Merrow</p>
  <p class="card-text person-title" style="left:467px; top:373px;">President &amp; CEO</p>

  <p class="card-text address" style="left:467px; top:414px;">4820 Calder Way,<br>Brookfield,<br>MD 20147</p>
  <p class="card-text contact" style="left:572px; top:414px;">
    <span>Phone:</span>410.555.0142<br>
    <span>Email:</span>dana@vetrune.com<br>
    <span>Web:</span>www.vetrune.com
  </p>

  <p class="card-text web" style="left:478px; top:783px;">www.vetrune.com</p>
</div>
</body>
</html>
```